Webbanner-Design für Führungskräfte-Coach
Danke für Ihr Engagement und die einwandfreie Abwicklung.
Zielgruppe
Ich coache Führungskräfte und Teams im Verkauf. Haupt-Keywort und Haupt-Thema:
Führung im Vertrieb. Das Design soll Führungskräften mit Verkaufsfunktionen gefallen.
Aufgabenstellung
Gemäss Memo (Datei: RBF-Banner-Memo).

```html
<!DOCTYPE html>
<html lang="de">
<head>
<meta charset="utf-8">
<title>Coach für Führungskräfte und Teams im Vertrieb</title>
<link rel="stylesheet" href="https://fonts.googleapis.com/css2?family=Open+Sans:ital,wght@0,400;0,600;1,400&display=swap">
<style>
  :root {
    --panel: #dde0e9;
    --ink: #1f1f22;
    --ink-soft: #3a3a40;
    --accent: #c8202a;
    --band: rgba(228, 230, 236, 0.88);
    --caption-band: rgba(232, 233, 237, 0.72);
    --brand-grey: #55575c;
    --photo-top: #9b9a99;
    --photo-mid: #c3c6cc;
    --photo-low: #a9acb3;
    --photo-bottom: #74767c;
  }
  * { margin: 0; padding: 0; box-sizing: border-box; }
  html, body { width: 1200px; height: 456px; overflow: hidden; background: var(--panel); }
  body { font-family: "Open Sans", Arial, sans-serif; color: var(--ink); }

  .banner { position: relative; width: 1200px; height: 456px; background: var(--panel); }

  .quote {
    position: absolute; left: 21px; top: 124px; width: 225px;
    font-style: italic; font-size: 16px; line-height: 29px; color: var(--ink);
  }
  .quote__author {
    display: block; text-align: right; margin-top: 12px; padding-right: 2px;
    font-style: italic; font-size: 14.5px; color: var(--ink-soft);
  }

  .stage { position: absolute; left: 258px; top: 0; width: 684px; height: 456px; overflow: hidden; }
  .stage__photo {
    position: absolute; inset: 0;
    background: linear-gradient(180deg, var(--photo-top) 0%, var(--photo-mid) 35%, var(--photo-low) 70%, var(--photo-bottom) 100%);
  }
  .brand-band {
    position: absolute; left: 0; top: 41px; width: 100%; height: 85px;
    background: var(--band);
    display: flex; align-items: center; padding-left: 16px; gap: 12px;
  }
  .brand-band__mark { width: 38px; height: 38px; background: var(--brand-grey); }
  .brand-band__name {
    border-left: 1px solid var(--brand-grey); padding-left: 10px;
    font-size: 17px; line-height: 22px; font-weight: 400; color: var(--brand-grey);
  }
  .caption-band {
    position: absolute; left: 0; top: 348px; width: 100%; height: 88px;
    background: var(--caption-band);
    display: flex; align-items: center; justify-content: center;
    padding-bottom: 2px;
  }
  .caption-band__title { font-size: 23.5px; font-weight: 600; color: var(--ink); }

  .services {
    position: absolute; left: 961px; top: 44px; width: 222px; list-style: none;
    font-size: 18px; line-height: 24.5px; color: var(--ink);
  }
  .services li { position: relative; padding-left: 12px; margin-bottom: 23px; }
  .services li::before {
    content: ""; position: absolute; left: 0; top: 10px;
    width: 5px; height: 5px; border-radius: 50%; background: var(--accent);
  }
</style>
</head>
<body>
<main class="banner">
  <blockquote class="quote">
    „Als Businesscoach und<br>Trainer unterstütze ich<br>Unternehmen dabei, wie sie<br>Ergebnisse im Umgang mit<br>Kunden verbessern und die<br>Kompetenzen dazu<br>kontinuierlich trainieren.”
    <cite class="quote__author">Roland Fehr</cite>
  </blockquote>

  <section class="stage">
    <div class="stage__photo" role="img" aria-label="Porträtfoto des Coaches vor einem Team im Besprechungsraum"></div>
    <div class="brand-band">
      <span class="brand-band__mark"></span>
      <span class="brand-band__name">Fehr<br>Coaching &amp; Training GmbH</span>
    </div>
    <div class="caption-band">
      <h1 class="caption-band__title">Coach für Führungskräfte und Teams im Vertrieb</h1>
    </div>
  </section>

  <ul class="services">
    <li>Führungs-System und<br>strategische Vorgaben</li>
    <li>Bildungskonzept und<br>Ausbildungsstandards</li>
    <li>Produktive Prozesse</li>
    <li>Verkaufskompetenzen</li>
    <li>Leadership-<br>Kompetenzen</li>
    <li>Ständiger Lern- und<br>Verbesserungsprozess</li>
  </ul>
</main>
</body>
</html>
```